Postcard Design

We need a postcard design for our 10 year anniversary open house. The company is Fernwood Medical Spa. The web site is www.fernwoodmedicalspa.com. We want royal blue, sliver and white colors for the postcard along with a 10 Year image.

It Company

```html
<!DOCTYPE html>
<html lang="en">
<head>
<meta charset="utf-8">
<title>Fernwood Medical Spa – 10 Year Open House Postcard</title>
<link rel="stylesheet" href="https://fonts.googleapis.com/css2?family=Ubuntu:wght@400;500;700&display=swap">
<style>
  :root {
    --royal: #4a62b8;
    --royal-light: #5f79cc;
    --lavender: #9aa4dc;
    --silver: #e4e5ea;
    --white: #ffffff;
    --ink: #4b4b4b;
    --charcoal: #3f3f41;
    --link: #3f56b0;
    --paper: #ecebe8;
  }
  * { margin: 0; padding: 0; box-sizing: border-box; }
  html, body { width: 825px; height: 1200px; overflow: hidden; }
  body {
    background: var(--paper);
    font-family: "Ubuntu", sans-serif;
    position: relative;
  }
  .card {
    position: absolute;
    width: 665px;
    box-shadow: 0 3px 10px rgba(0,0,0,.18);
    overflow: hidden;
  }
  .card-front { left: 80px; top: 125px; height: 431px; }
  .card-back  { left: 80px; top: 625px; height: 430px; }
  .card svg.art { position: absolute; inset: 0; }
  .txt { position: absolute; white-space: nowrap; }

  .headline { color: var(--white); font-weight: 700; letter-spacing: 1px; }
  .front-headline { left: 302px; top: 27px; font-size: 41px; }
  .front-tagline {
    right: 56px; top: 78px; text-align: right;
    color: var(--white); font-size: 15.5px; font-weight: 700; line-height: 24px;
  }
  .phone { color: var(--ink); font-weight: 700; }
  .front-phone { left: 215px; top: 296px; font-size: 26.5px; letter-spacing: .6px; }
  .web { color: var(--link); font-size: 17.5px; font-weight: 500; }
  .front-web { left: 217px; top: 330px; }
  .footer-note {
    left: 0; right: 0; top: 397px; text-align: center;
    color: var(--white); font-size: 16.5px; letter-spacing: 2px;
  }

  .brand { position: absolute; display: flex; align-items: center; gap: 6px; }
  .brand-dot { width: 12px; height: 12px; border-radius: 50%; background: var(--royal); flex: none; }
  .brand-name { color: var(--royal); font-size: 15px; font-weight: 500; line-height: 18px; }
  .front-brand { left: 535px; top: 298px; width: 120px; }
  .back-brand { left: 268px; top: 36px; width: 118px; }

  .back-headline { left: 0; width: 392px; text-align: center; top: 154px; font-size: 44px; }
  .back-phone { left: 0; width: 392px; text-align: center; top: 205px; font-size: 26px; color: var(--white); font-weight: 700; }
  .back-web { left: 38px; top: 374px; color: var(--white); font-size: 15px; }
</style>
</head>
<body>

<section class="card card-front" aria-label="Postcard front">
  <svg class="art" width="665" height="431" viewBox="0 0 665 431">
    <defs>
      <linearGradient id="silverFade" x1="0" y1="0" x2="0" y2="1">
        <stop offset="0" stop-color="#ffffff"/>
        <stop offset="1" stop-color="#e3e4e9"/>
      </linearGradient>
      <linearGradient id="royalFade" x1="0" y1="0" x2="1" y2="1">
        <stop offset="0" stop-color="#4a62b8"/>
        <stop offset="1" stop-color="#5a73c6"/>
      </linearGradient>
      <linearGradient id="heroFade" x1="0" y1="0" x2="1" y2="0">
        <stop offset="0" stop-color="#f0cdb8"/>
        <stop offset=".5" stop-color="#f6e4dc"/>
        <stop offset="1" stop-color="#fbf6f8"/>
      </linearGradient>
      <linearGradient id="badgeFade" x1="0" y1="0" x2="0" y2="1">
        <stop offset="0" stop-color="#cfe8f6"/>
        <stop offset=".6" stop-color="#e2f1d2"/>
        <stop offset="1" stop-color="#ececef"/>
      </linearGradient>
      <radialGradient id="facialFade"><stop offset="0" stop-color="#f7e7de"/><stop offset="1" stop-color="#e6c6b4"/></radialGradient>
      <radialGradient id="massageFade"><stop offset="0" stop-color="#f2dccd"/><stop offset="1" stop-color="#c99a80"/></radialGradient>
      <radialGradient id="flowerFade"><stop offset="0" stop-color="#fdfbf2"/><stop offset="1" stop-color="#b8d8da"/></radialGradient>
    </defs>
    <rect width="665" height="431" fill="url(#silverFade)"/>
    <rect x="0" y="0" width="285" height="190" fill="url(#heroFade)" role="img" aria-label="Photo of a smiling woman holding white orchids"/>
    <path d="M252 0 C212 60 268 125 222 190 L665 190 L665 0 Z" fill="url(#royalFade)"/>
    <path d="M252 0 C212 60 268 125 222 190" fill="none" stroke="#5b5b60" stroke-width="6"/>
    <rect x="0" y="188" width="665" height="17" fill="var(--lavender)"/>
    <rect x="0" y="381" width="665" height="6" fill="var(--lavender)"/>
    <rect x="0" y="387" width="665" height="44" fill="var(--charcoal)"/>
    <circle cx="305" cy="205" r="63" fill="var(--lavender)"/>
    <circle cx="305" cy="205" r="55" fill="url(#facialFade)" role="img" aria-label="Photo of a woman with a facial treatment"/>
    <circle cx="438" cy="205" r="63" fill="var(--lavender)"/>
    <circle cx="438" cy="205" r="55" fill="url(#massageFade)" role="img" aria-label="Photo of a relaxing massage"/>
    <circle cx="575" cy="205" r="63" fill="var(--lavender)"/>
    <circle cx="575" cy="205" r="55" fill="url(#flowerFade)" role="img" aria-label="Photo of frangipani flowers in a spa bowl"/>
    <rect x="33" y="225" width="158" height="133" rx="6" fill="url(#badgeFade)" role="img" aria-label="Celebrating 10 years anniversary emblem"/>
  </svg>

  <div class="txt headline front-headline">OPEN HOUSE</div>
  <div class="txt front-tagline">All the Luxury You Deserve with the<br>Medical Expertise You can Trust</div>

  <div class="txt phone front-phone">PHONE: 555.214.0190</div>
  <div class="txt web front-web">www.fernwoodmedicalspa.com</div>

  <div class="brand front-brand">
    <span class="brand-dot"></span>
    <span class="brand-name">Fernwood<br>Medical Spa</span>
  </div>

  <div class="txt footer-note">Please call for an appointment or complimentary consultation</div>
</section>

<section class="card card-back" aria-label="Postcard back">
  <svg class="art" width="665" height="430" viewBox="0 0 665 430">
    <defs>
      <linearGradient id="royalFadeBack" x1="0" y1="0" x2="1" y2="1">
        <stop offset="0" stop-color="#4a62b8"/>
        <stop offset="1" stop-color="#5a73c6"/>
      </linearGradient>
      <radialGradient id="portraitFade"><stop offset="0" stop-color="#f3dfd4"/><stop offset=".7" stop-color="#f8efea"/><stop offset="1" stop-color="#ffffff"/></radialGradient>
      <linearGradient id="badgeFadeBack" x1="0" y1="0" x2="0" y2="1">
        <stop offset="0" stop-color="#cfe8f6"/>
        <stop offset=".6" stop-color="#e2f1d2"/>
        <stop offset="1" stop-color="#f2f2f4"/>
      </linearGradient>
      <radialGradient id="smileFade"><stop offset="0" stop-color="#f6e6dc"/><stop offset="1" stop-color="#dcc0b0"/></radialGradient>
      <radialGradient id="restFade"><stop offset="0" stop-color="#f0d8c8"/><stop offset="1" stop-color="#bf927a"/></radialGradient>
      <radialGradient id="towelFade"><stop offset="0" stop-color="#ffffff"/><stop offset="1" stop-color="#e6d6cc"/></radialGradient>
    </defs>
    <rect width="665" height="430" fill="#ffffff"/>
    <rect x="18" y="16" width="100" height="84" rx="5" fill="url(#badgeFadeBack)" role="img" aria-label="Celebrating 10 years anniversary emblem"/>
    <rect x="135" y="12" width="115" height="120" fill="url(#portraitFade)" role="img" aria-label="Photo of a woman with a white lily in her hair"/>
    <path d="M0 130 C110 118 290 138 392 96 L392 292 L0 292 Z" fill="#e3e4ea"/>
    <path d="M0 136 C110 124 290 144 392 102 L392 292 L0 292 Z" fill="url(#royalFadeBack)"/>
    <rect x="0" y="290" width="392" height="140" fill="var(--charcoal)"/>
    <circle cx="80" cy="290" r="48" fill="var(--lavender)"/>
    <circle cx="80" cy="290" r="41" fill="url(#smileFade)" role="img" aria-label="Photo of a smiling woman"/>
    <circle cx="193" cy="290" r="48" fill="var(--lavender)"/>
    <circle cx="193" cy="290" r="41" fill="url(#restFade)" role="img" aria-label="Photo of a woman resting at a spa"/>
    <circle cx="305" cy="290" r="48" fill="var(--lavender)"/>
    <circle cx="305" cy="290" r="41" fill="url(#towelFade)" role="img" aria-label="Photo of a woman in a white towel"/>
    <rect x="392" y="0" width="8" height="370" fill="#d4d5d9"/>
    <rect x="290" y="370" width="375" height="60" fill="#ffffff"/>
    <rect x="577" y="34" width="59" height="59" fill="#d9d9db"/>
  </svg>

  <div class="brand back-brand">
    <span class="brand-dot"></span>
    <span class="brand-name">Fernwood<br>Medical Spa</span>
  </div>

  <div class="txt headline back-headline">OPEN HOUSE</div>
  <div class="txt back-phone">PHONE: 555.214.0190</div>
  <div class="txt back-web">www.fernwoodmedicalspa.com</div>
</section>

</body>
</html>
```